I need a book cover for a non-fiction book, entitled "Walk The Meadow Path and GLOW" (the "GLOW" is an acronym for "Gather Old Lantern Works" [but needn't {and probably shouldn't} be on the cover]).
The book will be 7" W X 10" H, in hardcover, and the spine will be 1.3" thick [just under "1-5/16"]).
When completed, I'll eventually need artwork for a full spread--of 16.874" W X 11.417" H--for back, spine and front artwork (see the two files attached, for specifics on final layout [feel free to concentrate only on the front cover, for the run-off selection process]).
The front cover by itself will measure 7.197" X 10.236" with bleed, trimmed to 7" X 10" for final size.
On the spine, the book title and author's last name (Pruitt) will be sufficient.
Author's name (Dale Pruitt) on the front cover, near the bottom/ bottom right, without great emphasis, generally preferred.
Don't need to worry about the back cover until finalists picked. I'll want a heading up top being probably a smaller version of the title.
In the body of the back page, I'll be putting in a text block (if necessary, to see the text), unless the background color is very light. Don't worry about having any graphics to speak of on the back, other than general light color, or screened image.
There will be a UPC bar code on the lower right of the back cover, also.

The book itself teaches the U.S. Constitution, to readers, covering the originally-ratified document (but not covering the amendments, which will be a separate volume, later), the founding principles of our American Republic (which doesn't rely upon voting or elections--Democracy--to uphold [so please don't emphasize the voting process in the artwork]).
A sincere patriotic theme (and colors, likely) would be preferred, along strict-construction themes (limited government of delegated powers, implemented using only necessary and proper means, to promote individual liberty and secured unalienable rights).
Christian perspective.
The Constitution, Bill of Rights, and Declaration of Independence are of course good graphics to include (but not any contemporary redesign of them).
American flags, eagles, gold and silver coin (but must be American-struck gold or silver coin design, from BEFORE 1933 [NOT the recent Harbor Finch bullion gold coins, or bullion silver eagles [which are coins, in 1 oz. weight, and its increments]) and historical-themed images of the Revolutionary era are fine, historical buildings okay, Liberty Bell okay. Statue of Liberty probably less desirable (since it doesn't directly relate to the Founders of the country, or the Framers of the Constitution, Bill of Rights, Declaration of Independence directly [even as it was meant to symbolize and honor them]).

The book is a compilation of my WalkTheMeadowPathEachSeason Program Course, an online video/audio/pdf Lesson that teaches the Constitution in one year (www.WalkTheMeadowPathEachSeason.com)

Patriotic conservative Christian men and women, typically older (but even older teens and young adults and serious college students

• Conservative patriot theme

```html
<!DOCTYPE html>
<html lang="en">
<head>
<meta charset="utf-8">
<title>Walk The Meadow Path and GLOW — Book Cover</title>
<link href="https://fonts.googleapis.com/css2?family=Anton&display=swap" rel="stylesheet">
<style>
  :root {
    --cover-bg: #ffffff;
    --patriot-red: #e52d27;
    --patriot-blue: #2e3f95;
  }
  html, body {
    margin: 0;
    padding: 0;
    width: 840px;
    height: 1200px;
    overflow: hidden;
    background: var(--cover-bg);
  }
  .book-cover {
    position: relative;
    width: 840px;
    height: 1200px;
    overflow: hidden;
    background: var(--cover-bg);
    font-family: "Anton", "Impact", sans-serif;
    text-transform: uppercase;
  }
  .title { margin: 0; font-weight: 400; }
  .title-line {
    position: absolute;
    display: block;
    line-height: 1;
    white-space: nowrap;
  }
  .title-line--walk {
    left: 136px;
    top: 186px;
    font-size: 110px;
    color: var(--patriot-red);
  }
  .title-line--subject {
    left: 34px;
    top: 322px;
    font-size: 104px;
    color: var(--patriot-blue);
  }
  .title-line--and {
    left: 228px;
    top: 450px;
    font-size: 106px;
    color: var(--patriot-red);
  }
  .title-line--acronym {
    left: 185px;
    top: 596px;
    font-size: 250px;
    letter-spacing: 10px;
    color: var(--patriot-red);
  }
  .author {
    position: absolute;
    left: 0;
    right: 0;
    top: 1090px;
    margin: 0;
    text-align: center;
    font-family: "Anton", "Impact", sans-serif;
    font-size: 52px;
    line-height: 1;
    color: var(--patriot-red);
    text-transform: none;
  }
</style>
</head>
<body>
  <main class="book-cover">
    <h1 class="title">
      <span class="title-line title-line--walk">Walk</span>
      <span class="title-line title-line--subject">The Meadow Path</span>
      <span class="title-line title-line--and">and</span>
      <span class="title-line title-line--acronym">GLOW</span>
    </h1>
    <p class="author">Dale Pruitt</p>
  </main>
</body>
</html>
```